Brochure Design Project

We need a brochure designed to introduce a new professional fitness testing programme we are launching. We are an established health and fitness club based in Wiltshire, England. We would like each design to use the company colours which are white, black and blue. We offer a premier service which we want the brochure to illustrate. We would like the brochure to be 4 x A5 pages (A4 paper folded in half) and landscape. We have attached a word document with the wording we want included and our company logo. Although we have placed page numbers at the bottom of each A5 side in the brief please do not include these in the brochure, this is simply to illustrate the order of the pages. What we need is for you to give the brochure colour, artwork and a professional touch while emphasising key points.
Updates

APOLIGIES TO ALL DESIGNERS....... please could the brochure be portrait.

Many thanks

Harbour Lane UK

Can we please have the desgines aimed more at amateur athletes as this is the market we are aiming at

thank you

More designs welcomed!

Reason: Very little designs recieved

Designers, thankyou soo much for your designs soo far. What we would like too see is rather than pictures of women and commercial images can we have images of professional looking cyclists please. many thanks

Target Market(s)

amateur fitness enthusiasts (male and female) between the ages of 25-50, in the upper socio-economic sector of society.

Industry/Entity Type

Fitness

Requirements
Must have
• The brochure must include the company logo and be 4 A5 lanscape pages (A4 folded in half). Only use the company colours: white, black and blue. (the blue is the colour on the website which is on the attatched word document/design brief). Must include pictures of professional looking cyclists and runners.
Nice to have
• A front page which is really creative and bold, which sells our service to the buyer in a respectable way.
Should not have
• Cheesey pictures.

```html
<!DOCTYPE html>
<html lang="en">
<head>
<meta charset="utf-8">
<title>Harbour Lane UK – Professional fitness testing brochure</title>
<link href="https://fonts.googleapis.com/css2?family=Arimo:ital,wght@0,400;0,700;1,400;1,700&display=swap" rel="stylesheet">
<style>
:root{
  --lavender:#b6bee3;
  --navy:#1f1f6b;
  --soft-blue:#6a78bd;
  --white:#ffffff;
  --track:#e8a68c;
  --track-light:#f0c0aa;
  --lane-blue:#3d6fc4;
  --grass:#7f8a52;
  --stage:#ffffff;
}
*{box-sizing:border-box;margin:0;padding:0}
html,body{width:1200px;height:1000px;overflow:hidden;background:var(--stage)}
body{font-family:"Arimo",Arial,sans-serif;color:var(--navy);position:relative}
.spread{position:absolute;left:260px;width:680px;height:480px;box-shadow:0 2px 10px rgba(0,0,0,.25)}
.spread--outside{top:14px;display:flex}
.spread--inside{top:506px;overflow:hidden}
.page{position:relative;width:340px;height:480px;background:var(--lavender)}
.page--back{border-right:1px solid rgba(31,31,107,.15)}
.wordmark{font-weight:700;color:var(--navy);letter-spacing:.5px}

/* back page */
.offer-title{position:absolute;top:108px;left:0;right:0;text-align:center;font-size:17px;font-weight:700;font-style:italic;line-height:1.15}
.price-box{position:absolute;top:163px;left:72px;width:198px;height:48px;background:var(--white);border-radius:5px;display:flex;align-items:center}
.price-box .cell{flex:1;text-align:center;font-size:9.5px;line-height:1.3;padding:0 4px}
.price-box .cell+.cell{border-left:1px solid var(--lavender);height:100%;display:flex;align-items:center;justify-content:center}
.price-box b{font-weight:700}
.discover{position:absolute;top:230px;left:0;right:0;text-align:center;font-size:12px;font-weight:700;font-style:italic}
.logo-bar{position:absolute;top:365px;left:72px;width:198px;height:36px;background:var(--white);border-radius:5px;display:flex;align-items:center;justify-content:center;gap:7px;font-size:13px}
.dot{width:9px;height:9px;border-radius:50%;background:var(--navy)}
.back-contact{position:absolute;top:410px;left:0;right:0;text-align:center;font-size:11px;font-weight:700;line-height:1.3}
.back-address{position:absolute;top:442px;left:0;right:0;text-align:center;font-size:8.5px;color:var(--soft-blue)}

/* front page */
.front-title{position:absolute;top:36px;left:24px;font-size:23px;font-weight:700;font-style:italic;line-height:1.02}
.logo-band{position:absolute;top:108px;left:0;width:200px;height:52px;background:var(--white);border-radius:0 6px 6px 0;display:flex;align-items:center;justify-content:center;gap:7px;font-size:13px}
.tagline{position:absolute;top:196px;left:24px;font-size:12.5px;font-weight:700;font-style:italic}
.benefits{position:absolute;top:236px;left:24px;width:190px}
.benefits h2{font-size:11px;font-weight:700;line-height:1.25;margin-bottom:5px}
.benefits ul{list-style:none;font-size:9px;color:var(--soft-blue);line-height:1.35}
.benefits li::before{content:"• ";color:var(--soft-blue)}
.photo-column{position:absolute;top:32px;right:20px;width:102px;display:flex;flex-direction:column;gap:4px}
.photo{height:67px;border-radius:4px}
.photo--sprint-start{background:linear-gradient(180deg,#b34a33,#8a3a2a)}
.photo--road-cyclist{background:linear-gradient(180deg,#9ab0d4,#6f7d5c)}
.photo--hurdler{background:linear-gradient(180deg,#6c8a3c,#b04b3a)}
.photo--track-cyclists{background:linear-gradient(180deg,#e7a087,#4a6cbc)}
.photo--sprinter{background:linear-gradient(180deg,#b9b4b0,#6a8a3a)}
.front-footer{position:absolute;top:395px;left:18px;right:18px;height:52px;background:var(--white);border-radius:6px;padding:9px 12px}
.front-footer .line{display:flex;justify-content:space-between;font-size:12px;font-weight:700}
.front-footer .address{font-size:8.5px;color:var(--soft-blue);margin-top:4px}

/* inside spread */
.track-photo{position:absolute;inset:0;background:linear-gradient(180deg,var(--track-light) 0%,var(--track) 62%,#d99077 74%,var(--lane-blue) 88%,var(--grass) 100%)}
.intro-tab{position:absolute;top:28px;left:18px;width:206px;height:58px;background:var(--lavender);border-radius:6px 6px 0 0;padding:9px 12px;font-size:11px;font-weight:700;font-style:italic;line-height:1.2}
.process-band{position:absolute;top:28px;left:230px;right:0;height:58px;background:var(--lavender);border-radius:6px 0 0 0;padding:34px 10px 0;font-size:11px;font-weight:700;font-style:italic}
.intro-copy{position:absolute;top:98px;left:30px;width:186px;font-size:8px;font-style:italic;line-height:1.38;color:var(--white)}
.intro-copy b{font-weight:700}
.stages{position:absolute;top:98px;left:236px;right:20px;display:flex;gap:8px}
.stage{flex:1}
.stage h3{font-size:8.5px;font-weight:700;line-height:1.2;border-bottom:1px solid var(--navy);padding-bottom:2px;margin-bottom:4px;min-height:26px;display:flex;flex-direction:column;justify-content:flex-end}
.stage ul{list-style:none;font-size:7.5px;line-height:1.3}
.stage li{padding-left:7px;text-indent:-7px}
.stage li::before{content:"• "}
</style>
</head>
<body>

<section class="spread spread--outside">
  <div class="page page--back">
    <h2 class="offer-title">Professional fitness testing<br>at affordable prices</h2>
    <div class="price-box">
      <div class="cell">Single test for<br>just <b>£55</b></div>
      <div class="cell">One test every<br>12 weeks for <b>£150</b></div>
    </div>
    <p class="discover">Discover your potential today</p>
    <div class="logo-bar"><span class="dot"></span><span class="wordmark">Harbour Lane UK</span></div>
    <p class="back-contact">01632 960418<br>www.harbourlaneukgym.com</p>
    <p class="back-address">Unit 7, Brookmead Trading estate, Marlow Vale, Wiltshire, SN99 4QT</p>
  </div>

  <div class="page page--front">
    <h1 class="front-title">Professional<br>fitness testing</h1>
    <div class="logo-band"><span class="dot"></span><span class="wordmark">Harbour Lane UK</span></div>
    <p class="tagline">Become the best you can!</p>
    <div class="benefits">
      <h2>Understand your fitness...<br>Achieve peak performance</h2>
      <ul>
        <li>Cardiovascular efficiency</li>
        <li>Lactate threshold</li>
        <li>VO2 max</li>
        <li>Qualified exercise specialists</li>
      </ul>
    </div>
    <div class="photo-column">
      <div class="photo photo--sprint-start" role="img" aria-label="Sprinter's hands on the track at the starting line"></div>
      <div class="photo photo--road-cyclist" role="img" aria-label="Road cyclist riding in the hills"></div>
      <div class="photo photo--hurdler" role="img" aria-label="Athlete clearing a hurdle"></div>
      <div class="photo photo--track-cyclists" role="img" aria-label="Track cyclists racing on a velodrome"></div>
      <div class="photo photo--sprinter" role="img" aria-label="Sprinter crossing the finish line"></div>
    </div>
    <div class="front-footer">
      <div class="line"><span>01632 960418</span><span>www.harbourlaneukgym.com</span></div>
      <p class="address">Unit 7, Brookmead Trading estate, Marlow Vale, Wiltshire, SN99 4QT</p>
    </div>
  </div>
</section>

<section class="spread spread--inside">
  <div class="track-photo" role="img" aria-label="Team of track cyclists riding in line on a velodrome"></div>
  <h2 class="intro-tab">How do you get to where<br>you want to be without<br>knowing where you are?</h2>
  <h2 class="process-band">Our four stage process...</h2>
  <p class="intro-copy">At <b>Harbour Lane UK</b> we care about your fitness goals, which is why we have introduced our new and exciting comprehensive fitness assessment. Our qualified exercise specialists are on hand to take you through our four stage process. Furthermore, the variety of testing protocols we utilise are all used by professional athletes. With our help, you can achieve your desired success and continuously develop. This is achieved through a combination of energy and direction as well as a balance between hard work and recovery.</p>
  <div class="stages">
    <div class="stage">
      <h3><span>1</span><span>Pre-test analysis</span></h3>
      <ul>
        <li>Body fat percentage</li>
        <li>Lean mass calculation</li>
        <li>Blood Pressure (ml/kg)</li>
        <li>Pulse (bpm)</li>
        <li>Cholesterol (measure)</li>
        <li>Lung function assessment (FEV1)</li>
      </ul>
    </div>
    <div class="stage">
      <h3><span>2</span><span>Fitness test</span></h3>
      <ul>
        <li>Cycling, running or rowing</li>
        <li>Vo2 max (ml/kg/g)</li>
        <li>Lactate threshold</li>
        <li>Cardiovascular efficiency</li>
        <li>Pedalling assessment for cyclists</li>
        <li>Flexibility tests</li>
      </ul>
    </div>
    <div class="stage">
      <h3><span>3</span><span>Post test report</span></h3>
      <ul>
        <li>Consultation with your assigned specialist</li>
        <li>Detailed test results</li>
        <li>Comparisons made with normative data</li>
        <li>Concluding with areas to develop</li>
      </ul>
    </div>
    <div class="stage">
      <h3><span>4</span><span>12 week programme</span></h3>
      <ul></ul>
    </div>
  </div>
</section>

</body>
</html>
```